Transport & Storage Company needs a revamp of current card

Would like to keep same colours & basic design but would like to "sharpen" up look of card.

Please remove "The Bright Haulers"

Please add 1800 419 386 on front & back of card

Please add email address on back of card - martin@brackenfreight.com.au

I would like our ABN No - 83 214 976 302 on back of card (which currently has logo only). Logo on back of card can be removed if insufficient space.

Please design another card (same as above) but with Donna Petherick - 0438 562 714, donna@brackenfreight.com.au

I do not want cards to look "too busy" so please re-arrange layout of card if necessary.

Target Market(s)

Transport & Storage

Industry/Entity Type

It Company

Contact Information for Business Card

Please refer to attached current business card

Font styles to use
Other font styles liked:
• Tahoma

Requirements
Must have
• Refer to project decsription
Nice to have
Should not have

```html
<!DOCTYPE html>
<html lang="en">
<head>
<meta charset="utf-8">
<title>Bracken Freight – Business Cards</title>
<link rel="stylesheet" href="https://fonts.googleapis.com/css2?family=Source+Sans+3:wght@400;700&family=Dancing+Script:wght@700&display=swap">
<style>
  :root {
    --purple: #76388c;
    --grey: #57575a;
    --paper: #ffffff;
    --backdrop: #e9e8ea;
    --card-w: 540px;
    --card-h: 309px;
  }
  * { box-sizing: border-box; margin: 0; padding: 0; }
  html, body {
    width: 1200px;
    height: 892px;
    overflow: hidden;
    background: var(--backdrop);
  }
  .sheet {
    position: relative;
    width: 1200px;
    height: 892px;
    display: flex;
    align-items: center;
    justify-content: center;
    gap: 40px;
  }
  .card {
    position: relative;
    width: var(--card-w);
    height: var(--card-h);
    background: var(--paper);
    overflow: hidden;
    box-shadow: 0 2px 10px rgba(0,0,0,0.12);
  }
  .card__stripes {
    position: absolute;
    inset: 0;
    width: 100%;
    height: 100%;
  }
  .brand {
    position: absolute;
    display: flex;
    align-items: center;
    gap: 12px;
    font-family: "Source Sans 3", Tahoma, sans-serif;
    font-weight: 700;
    color: var(--purple);
    white-space: nowrap;
  }
  .brand__dot {
    border-radius: 50%;
    background: var(--purple);
    flex: none;
  }
  .card--front .brand { top: 48px; right: 40px; font-size: 44px; }
  .card--front .brand__dot { width: 34px; height: 34px; }
  .card--back .brand { top: 36px; left: 200px; font-size: 34px; }
  .card--back .brand__dot { width: 26px; height: 26px; }

  .contact {
    position: absolute;
    list-style: none;
    font-family: "Source Sans 3", Tahoma, sans-serif;
    font-weight: 400;
    font-size: 14px;
    line-height: 20px;
    color: var(--purple);
  }
  .card--front .contact { left: 30px; bottom: 78px; }
  .card--back .contact { right: 34px; bottom: 38px; text-align: right; }
  .contact__gap { height: 14px; }

  .person {
    position: absolute;
    right: 34px;
    top: 150px;
    font-family: "Dancing Script", cursive;
    font-weight: 700;
    font-size: 30px;
    color: var(--purple);
  }
</style>
</head>
<body>
<main class="sheet">

  <section class="card card--front" aria-label="Card front">
    <svg class="card__stripes" viewBox="0 0 540 309" aria-hidden="true">
      <polygon points="150,309 540,148 540,172 196,309" fill="var(--grey)"/>
      <polygon points="214,309 540,190 540,309" fill="var(--purple)"/>
    </svg>
    <div class="brand"><span class="brand__dot"></span>Bracken Freight</div>
    <ul class="contact">
      <li>1800 419 386</li>
      <li>martin@brackenfreight.com.au</li>
      <li>ABN No - 83 214 976 302</li>
    </ul>
  </section>

  <section class="card card--back" aria-label="Card back">
    <svg class="card__stripes" viewBox="0 0 540 309" aria-hidden="true">
      <polygon points="120,0 160,0 192,309 176,309" fill="var(--grey)"/>
      <polygon points="0,100 0,309 150,309" fill="var(--purple)"/>
    </svg>
    <div class="brand"><span class="brand__dot"></span>Bracken Freight</div>
    <p class="person">Martin Hollis</p>
    <ul class="contact">
      <li>www.brackenfreight.com.au</li>
      <li class="contact__gap"></li>
      <li>0412 730 558</li>
      <li>1800 419 386</li>
    </ul>
  </section>

</main>
</body>
</html>
```